Mexican Restaurant needs a new Menu Design

Mexican restaurant LA TORTUGA VERDE is renewing its menu, so we need something new.
Since our inception we have given the task of rescuing ingredients, recipes, and traditional and representatives dishes of the culinary techniques of yesteryear.
We are the only restaurant in Guadalajara that manufactures its own dairy natural as fresh cheese, the cream and our already well-known and traditional jocoqui. In addition, we produce organic ranch egg and are currently in the development of organic vegetables cultivated on the slopes of the old Hill which gives our plants benefit from an exceptional microclimate.
Find more information about the restaurant in www.latortugaverde.com.
The menu needs to have the full list of products with the prices, some phrases that speak of the philosophy of the ranch-style-living, photos.
We need the cover, back cover and interiors.
Updates
Thank you so much for the proposals you have submitted for the menu design. We are looking them carefully.
Thank you very much for taking your time to design a proposal for our menu!!!
Target Market(s)
The target is very wide (28-40 yrs.): Young executives, Young families, Housewives.
Industry/Entity Type
Restaurant
Look and feel
Each slider illustrates characteristics of the customer's brand and the style your logo design should communicate.

```html
<!DOCTYPE html>
<html lang="en">
<head>
<meta charset="utf-8">
<title>La Tortuga Verde – Menu</title>
<link rel="stylesheet" href="https://fonts.googleapis.com/css2?family=Cinzel:wght@400&family=Lobster&family=Arimo:wght@400;700&display=swap">
<style>
  :root {
    --red-deep: #d81405;
    --red-bright: #ff2a10;
    --red-warm: #e8361c;
    --panel: #fde8e8;
    --panel-border: #e8170a;
    --ink: #111111;
    --logo-text: #ffffff;
    --photo-brown: #6b3a24;
    --photo-dark: #3b2a22;
    --photo-food: #9a7a4a;
    --mascot: #a51d34;
  }
  * { box-sizing: border-box; margin: 0; padding: 0; }
  html, body { width: 768px; height: 1200px; overflow: hidden; }
  body { font-family: "Arimo", Arial, sans-serif; color: var(--ink); background: var(--red-deep); }
  .menu-page { position: relative; width: 768px; height: 1200px; overflow: hidden; }

  .backdrop-smoke {
    position: absolute; inset: 0;
    background:
      radial-gradient(ellipse 60% 25% at 50% 10%, #b80e04 0%, transparent 70%),
      radial-gradient(ellipse 50% 30% at 20% 20%, #ff3a1a 0%, transparent 70%),
      linear-gradient(180deg, var(--red-deep) 0%, var(--red-bright) 40%, var(--red-warm) 100%);
  }
  .photo-beans {
    position: absolute; left: 0; top: 282px; width: 212px; height: 240px;
    background: linear-gradient(135deg, var(--photo-dark), var(--photo-brown));
  }
  .photo-side {
    position: absolute; left: 740px; top: 990px; width: 28px; height: 140px;
    background: linear-gradient(180deg, #e9e2d6, var(--photo-food));
  }
  .photo-dish {
    position: absolute; left: 220px; top: 1120px; width: 548px; height: 80px;
    background: linear-gradient(90deg, #e8e4dc 0%, #8a9a4a 25%, #6b4a30 55%, #a0603a 80%, #f2efe8 100%);
  }

  .brand {
    position: absolute; left: 170px; top: 74px; width: 400px; height: 142px;
    display: flex; align-items: center; justify-content: center;
  }
  .brand-name {
    font-family: "Cinzel", Georgia, serif; font-weight: 400;
    font-size: 34px; color: var(--logo-text); letter-spacing: 1px;
  }

  .menu-panel {
    position: absolute; left: 15px; top: 363px; width: 735px; height: 763px;
    background: var(--panel); border: 3px solid var(--panel-border); border-radius: 9px;
  }
  .mascot {
    position: absolute; border-radius: 50% 50% 40% 40%;
    background: radial-gradient(circle at 50% 35%, #c88a3a 0%, var(--mascot) 60%, transparent 72%);
  }
  .mascot-top { left: 0; top: 363px; width: 147px; height: 142px; }
  .mascot-bottom { left: 0; top: 1057px; width: 158px; height: 143px; }

  .menu-title {
    position: absolute; left: 243px; top: 360px; width: 240px; text-align: center;
    font-family: "Lobster", cursive; font-size: 86px; line-height: 1; color: #222;
    text-shadow: 2px 3px 3px rgba(0,0,0,0.35);
  }

  .menu-column { position: absolute; top: 530px; list-style: none; }
  .menu-column h2 { font-size: 17px; font-weight: 700; letter-spacing: 0.3px; margin-bottom: 12px; }
  .menu-column li { font-size: 13.5px; line-height: 30px; }
  .col-morning { left: 52px; }
  .col-afternoon { left: 317px; }
  .col-evening { left: 534px; }

  .featured-dish { position: absolute; left: 53px; top: 884px; width: 660px; }
  .featured-dish h3 { font-size: 21.5px; font-weight: 700; margin-bottom: 6px; }
  .featured-dish p { font-size: 17px; line-height: 30px; }
</style>
</head>
<body>
<main class="menu-page">
  <div class="backdrop-smoke" role="img" aria-label="Red smoky textured background"></div>
  <div class="photo-beans" role="img" aria-label="Photo of refried beans and a bowl"></div>
  <div class="photo-side" role="img" aria-label="Photo of a plated dish"></div>
  <div class="photo-dish" role="img" aria-label="Photo of chilaquiles with lime wedges and cheese"></div>

  <header class="brand">
    <span class="brand-name">LA TORTUGA VERDE</span>
  </header>

  <section class="menu-panel"></section>
  <div class="mascot mascot-top" role="img" aria-label="Cartoon chip mascot with sombrero and lasso"></div>

  <h1 class="menu-title">Menu</h1>

  <ul class="menu-column col-morning">
    <h2>POR LA MANANA</h2>
    <li>Chilaquiles'n</li>
    <li>Blanquillos</li>
    <li>The Tamales'n</li>
    <li>The Sopes'n</li>
    <li>The BBW</li>
    <li>Muffins and semes</li>
    <li>From juera</li>
    <li>Children Breakfast</li>
  </ul>
  <ul class="menu-column col-afternoon">
    <h2>POR LA TRADE</h2>
    <li>Pa 'Start</li>
    <li>Quesadillas</li>
    <li>Salads</li>
    <li>Soups</li>
    <li>The Best World Birria</li>
    <li>Enchiladas'n</li>
    <li>Our grill</li>
    <li>Dishes Juertes</li>
  </ul>
  <ul class="menu-column col-evening">
    <h2>POR LA MANANA</h2>
    <li>Pa 'Start</li>
    <li>Quesadillas</li>
    <li>Salads</li>
    <li>Soups</li>
    <li>The Best World Birria</li>
    <li>Enchiladas'n</li>
    <li>Our grill</li>
    <li>Dishes Juertes</li>
  </ul>

  <article class="featured-dish">
    <h3>Verdis Chilaquiles With Language</h3>
    <p>A Generous Portion of Verdis Chilaquiles with Beef Tongue Frijolitos accompanied by La Casa. Bring chopped white onions on top.</p>
  </article>

  <div class="mascot mascot-bottom" role="img" aria-label="Cartoon chip mascot with sombrero and lasso"></div>
</main>
</body>
</html>
```